Modern CNC Machining Facility in Need of Web Site Improvement

Brixton Fabrication and Tooling, LLC is in need of a web site update. We need to highlight both product sales and our manufacturing services offered. We have recently started offering online product sales and need a better ecommerce platform for our customers. We would like the design winner to be able to freelance the project to a fully functioning webpage.
www.brixtonfabrication.example
What we like about our current web site:
Black and red highlight colors
Gear and caliper logo
RNVR Veteran owned business
What we don't like about our current web site:
Unorganized
Doesn't stand out
Looks like it was made in 1995
Online Product sales are awkward

```html
<!DOCTYPE html>
<html lang="en">
<head>
<meta charset="utf-8">
<title>Brixton Fabrication and Tooling, LLC</title>
<link rel="stylesheet" href="https://fonts.googleapis.com/css2?family=Arimo:wght@400;700&family=Open+Sans:wght@400;600&display=swap">
<style>
:root{
  --red:#c4161c;
  --red-dark:#9a1116;
  --red-bright:#e8262b;
  --ink:#1a1a1a;
  --grey-text:#333;
  --muted:#8a8a8a;
  --panel:#ececec;
  --line:#d5d5d5;
  --white:#fff;
}
*{box-sizing:border-box;margin:0;padding:0}
html,body{width:1159px;height:1200px;overflow:hidden;background:#fff}
body{position:relative;font-family:"Open Sans",sans-serif;color:var(--grey-text)}

.site-header{position:absolute;left:0;top:0;width:1159px;height:135px;background:linear-gradient(#fff 0%,#f6f6f6 60%,#e4e4e4 100%);border-top:4px solid #555;border-bottom:1px solid #cfcfcf}
.brand{position:absolute;left:58px;top:26px;display:flex;align-items:center;gap:10px;width:340px}
.brand-mark{width:44px;height:44px;border-radius:50%;background:var(--red);border:6px solid #2a2a2a;flex:none}
.brand-name{font-family:"Arimo",sans-serif;font-weight:700;font-size:17px;line-height:21px;color:var(--red-dark)}
.phone-tab{position:absolute;left:859px;top:-4px;width:237px;height:34px;background:linear-gradient(#6d6d6d,#4a4a4a);border:2px solid #ddd;border-top:none;border-radius:0 0 12px 12px;display:flex;align-items:center;gap:12px;padding-left:26px;color:#fff;font-family:"Arimo",sans-serif;font-size:16px}
.main-nav{position:absolute;left:463px;top:79px;display:flex;align-items:center;font-family:"Arimo",sans-serif;font-size:14.5px;color:#2a2a2a}
.main-nav a{color:inherit;text-decoration:none;padding:0 20px;line-height:32px}
.main-nav a.active{background:var(--red-dark);color:#fff;font-weight:700;padding:0 23px;border:2px solid #fff;outline:1px solid #bbb;margin-right:6px}

.hero{position:absolute;left:0;top:135px;width:1159px;height:321px;background:linear-gradient(#b5141a 0%,#d21f25 45%,#a3131a 100%);overflow:hidden}
.hero-copy{position:absolute;left:54px;top:42px;width:400px;color:#fff;font-family:"Arimo",sans-serif}
.hero-copy h1{font-size:22.5px;line-height:38px;font-weight:700}
.hero-copy p{margin-top:28px;font-size:14px;line-height:21px}
.hero-art{position:absolute;left:0;top:0}

.lead-form{position:absolute;left:0;top:456px;width:1159px;height:106px;background:linear-gradient(#3a3a3a,#151515);display:flex;align-items:center;padding-left:57px;gap:47px}
.lead-form .field{width:228px;height:33px;background:#f2f2f2;border:1px solid #ccc;font-family:"Arimo",sans-serif;font-size:14.5px;color:#8a8a8a;padding:0 9px;display:flex;align-items:center}
.lead-form .field:nth-child(2),.lead-form .field:nth-child(3){margin-left:-2px}
.submit{width:150px;height:35px;background:linear-gradient(var(--red-bright),var(--red-dark));border:1px solid #7e0c10;color:#fff;font-family:"Arimo",sans-serif;font-size:18px;letter-spacing:.5px;display:flex;align-items:center;justify-content:center;margin-left:6px}

.product-menu{position:absolute;left:66px;top:586px;width:274px;height:455px;background:linear-gradient(90deg,#f4f4f4,#e8e8e8);border:1px solid #ddd;border-radius:8px}
.product-menu h2{position:absolute;left:-5px;top:10px;width:266px;height:32px;background:linear-gradient(#4a4a4a,#0e0e0e);color:#fff;font-family:"Open Sans",sans-serif;font-weight:600;font-size:17px;display:flex;align-items:center;gap:6px;padding-left:8px}
.menu-icon{width:20px;height:20px;background:#fff;border-radius:3px;display:flex;align-items:center;justify-content:center}
.product-menu ul{position:absolute;left:10px;top:46px;width:248px;list-style:none}
.product-menu li{height:31.6px;border-bottom:1px dotted #555;display:flex;align-items:center;gap:9px;font-size:11px;color:#222}
.product-menu li:last-child{border-bottom:none}
.bullet{width:14px;height:13px;background:var(--red-bright);color:#fff;font-size:9px;line-height:13px;text-align:center}

.catalog{position:absolute;left:374px;top:588px;width:694px;height:452px;background:#e6e6e6;border:1px dotted #aaa;display:grid;grid-template-columns:repeat(3,208px);grid-template-rows:repeat(2,210px);gap:12px 21px;padding:6px 11px}
.product-card{background:linear-gradient(#fafafa,#efefef);border:1px solid #d8d8d8;border-radius:3px;position:relative;text-align:center}
.product-photo{width:66px;height:116px;margin:8px auto 0;background:linear-gradient(90deg,#5a5a5a,#c9c9c9 50%,#4b4b4b);border-radius:4px 4px 2px 2px}
.product-name{margin-top:5px;font-size:11px;color:var(--red);letter-spacing:.2px}
.product-spec{font-size:11px;color:#222;margin-top:1px}
.product-foot{position:absolute;left:22px;right:20px;bottom:14px;display:flex;justify-content:space-between;align-items:center}
.price{font-size:21px;color:var(--muted);font-family:"Open Sans",sans-serif}
.detail-btn{width:74px;height:28px;background:var(--red-bright);border:2px solid #fff;outline:1px solid var(--red-bright);color:#fff;font-size:16px;display:flex;align-items:center;justify-content:center}

.site-footer{position:absolute;left:0;top:1075px;width:1159px;height:125px;background:#0b0b0b;border-top:3px solid var(--red)}
.partners{position:absolute;left:292px;top:24px;display:flex;gap:18px;align-items:center}
.partners span{display:block;height:20px;background:#5a5a5a;border-radius:3px}
.footer-links{position:absolute;left:0;top:71px;width:1159px;text-align:center;font-size:12.5px;letter-spacing:1px;color:#ddd}
.copyright{position:absolute;left:0;top:100px;width:1159px;text-align:center;font-size:12px;letter-spacing:1px;color:#ccc}
</style>
</head>
<body>

<header class="site-header">
  <div class="brand">
    <span class="brand-mark"></span>
    <span class="brand-name">Brixton Fabrication and Tooling, LLC</span>
  </div>
  <div class="phone-tab">
    <svg width="20" height="22" viewBox="0 0 20 22" aria-hidden="true"><rect x="1" y="1" width="6" height="20" rx="2" fill="#fff"/><rect x="9" y="4" width="10" height="16" rx="1" fill="none" stroke="#fff" stroke-width="1.6"/><rect x="11" y="6" width="6" height="3" fill="#fff"/><g fill="#fff"><rect x="11" y="11" width="2" height="2"/><rect x="15" y="11" width="2" height="2"/><rect x="11" y="15" width="2" height="2"/><rect x="15" y="15" width="2" height="2"/></g></svg>
    555-014-2738
  </div>
  <nav class="main-nav">
    <a class="active">Home</a>
    <a>Online Product Sales</a>
    <a>Ice Fishing Spears</a>
    <a>About Us</a>
    <a>Contact Us</a>
  </nav>
</header>

<section class="hero">
  <div class="hero-copy">
    <h1>We are your CNC milling and turning go-to facility.</h1>
    <p>Our manufacturing facility is located in Lakeshore Bay, Michigan and is equipped to perform a variety of machining services, including three axis CNC milling, "lights out" CNC turning, CNC Plasma Cutting, fully automatic sawing, prototype machining, long and short run production.</p>
  </div>
  <svg class="hero-art" width="1159" height="321" viewBox="0 0 1159 321">
    <defs>
      <linearGradient id="sceneTone" x1="0" y1="0" x2="0" y2="1">
        <stop offset="0" stop-color="#b9cde0"/>
        <stop offset="0.35" stop-color="#9aa7b2"/>
        <stop offset="0.6" stop-color="#d8dde2"/>
        <stop offset="1" stop-color="#a9b0b6"/>
      </linearGradient>
    </defs>
    <circle cx="772" cy="160" r="286" fill="none" stroke="#ef4a4e" stroke-width="7"/>
    <circle cx="772" cy="160" r="279" fill="url(#sceneTone)" role="img" aria-label="Photo of an ice fisherman in a yellow suit seated beside a hole on a frozen lake"/>
    <g>
      <circle cx="493" cy="150" r="18" fill="#eee" stroke="#bbb"/>
      <path d="M497 141 L488 150 L497 159" fill="none" stroke="#999" stroke-width="3"/>
      <circle cx="1047" cy="159" r="18" fill="#eee" stroke="#bbb"/>
      <path d="M1043 150 L1052 159 L1043 168" fill="none" stroke="#999" stroke-width="3"/>
    </g>
  </svg>
</section>

<section class="lead-form" aria-label="Request a quote">
  <div class="field">Name</div>
  <div class="field">Email</div>
  <div class="field">Phone</div>
  <div class="submit">SUBMIT</div>
</section>

<aside class="product-menu">
  <h2><span class="menu-icon"><svg width="14" height="14" viewBox="0 0 14 14" aria-hidden="true"><path d="M5 9 L9 5 M4 7 L2 9 a2 2 0 0 0 3 3 L7 10 M10 7 L12 5 a2 2 0 0 0 -3 -3 L7 4" fill="none" stroke="#333" stroke-width="1.6"/></svg></span>Our Products</h2>
  <ul>
    <li><span class="bullet">›</span>Drilling</li>
    <li><span class="bullet">›</span>Boring</li>
    <li><span class="bullet">›</span>Tapping</li>
    <li><span class="bullet">›</span>Milling</li>
    <li><span class="bullet">›</span>CNC Turning</li>
    <li><span class="bullet">›</span>CNC Milling</li>
    <li><span class="bullet">›</span>CNC Plasma Cutting</li>
    <li><span class="bullet">›</span>Sawing</li>
    <li><span class="bullet">›</span>Boring</li>
    <li><span class="bullet">›</span>Tapping</li>
    <li><span class="bullet">›</span>Milling</li>
    <li><span class="bullet">›</span>CNC Turning</li>
    <li><span class="bullet">›</span>CNC Milling</li>
  </ul>
</aside>

<main class="catalog">
  <article class="product-card"><div class="product-photo" role="img" aria-label="Steel ice fishing spear head"></div><div class="product-name">Northline 230 BLADE 9 X 48T</div><div class="product-spec">X 1 For Cutting Steel</div><div class="product-foot"><span class="price">$99.99</span><span class="detail-btn">Detail</span></div></article>
  <article class="product-card"><div class="product-photo" role="img" aria-label="Steel ice fishing spear head"></div><div class="product-name">Northline 230 BLADE 9 X 48T</div><div class="product-spec">X 1 For Cutting Steel</div><div class="product-foot"><span class="price">$99.99</span><span class="detail-btn">Detail</span></div></article>
  <article class="product-card"><div class="product-photo" role="img" aria-label="Steel ice fishing spear head"></div><div class="product-name">Northline 230 BLADE 9 X 48T</div><div class="product-spec">X 1 For Cutting Steel</div><div class="product-foot"><span class="price">$99.99</span><span class="detail-btn">Detail</span></div></article>
  <article class="product-card"><div class="product-photo" role="img" aria-label="Steel ice fishing spear head"></div><div class="product-name">Northline 230 BLADE 9 X 48T</div><div class="product-spec">X 1 For Cutting Steel</div><div class="product-foot"><span class="price">$99.99</span><span class="detail-btn">Detail</span></div></article>
  <article class="product-card"><div class="product-photo" role="img" aria-label="Steel ice fishing spear head"></div><div class="product-name">Northline 230 BLADE 9 X 48T</div><div class="product-spec">X 1 For Cutting Steel</div><div class="product-foot"><span class="price">$99.99</span><span class="detail-btn">Detail</span></div></article>
  <article class="product-card"><div class="product-photo" role="img" aria-label="Steel ice fishing spear head"></div><div class="product-name">Northline 230 BLADE 9 X 48T</div><div class="product-spec">X 1 For Cutting Steel</div><div class="product-foot"><span class="price">$99.99</span><span class="detail-btn">Detail</span></div></article>
</main>

<footer class="site-footer">
  <div class="partners" aria-label="Partner badges">
    <span style="width:62px"></span><span style="width:82px"></span><span style="width:54px"></span><span style="width:34px"></span><span style="width:72px"></span><span style="width:86px"></span><span style="width:72px"></span>
  </div>
  <div class="footer-links">Home | Login | Specials | Shopping Cart | Checkout | Contact us | Terms | Privacy Notice | Shipping</div>
  <div class="copyright">Copyright brixtonfabrication.example, 2011</div>
</footer>

</body>
</html>
```